WEBSITE REFRESH / REDESIGN- USE OLD WEBSITE TO CONSTRUCT NEW TEMPLATE

The current website was designed years ago, and we is now outdated.

We are looking for an updated design to our old website. We are looking for something that is consumer friendly, shows sophistication and is pleasing to the eye and modern.

Our old website consists of 25 pages. You are not required to design new text other from copying and pasting the current text and images.

The redesign requires the site to be modern, easy to navigate.

The current website is: www.brelvoxlumber.com.au, every page must be included and titled the same as the old one.

The home page requires a large slider, that I can change easily often.

Any new ideas are welcome.

I do have a template that I have purchased, however this isn't required to be used....any new exciting ideas will be considered.

Target Market(s)

existing customers; new customers demonstrating what we are offering to sell

Coding

Coded - Design and coding required

Font styles to use
Sans Serif

Colors
85cae6
33a6d7
0293ce
86cfc6
33b8a4
add136
fbee3e
fbf289
faa54b

Requirements
Must have
• text and photos from existing site. every page needs to be included in redesign.

```html
<!DOCTYPE html>
<html lang="en">
<head>
<meta charset="utf-8">
<title>Brelvox Lumber – Timber Fencing &amp; Decking</title>
<link rel="stylesheet" href="https://fonts.googleapis.com/css2?family=Poppins:wght@400;500;600;700&family=Open+Sans:wght@400;600&display=swap">
<style>
:root{
  --sky:#85cae6;
  --blue:#33a6d7;
  --deep-blue:#0293ce;
  --mint:#86cfc6;
  --teal:#33b8a4;
  --lime:#add136;
  --yellow:#fbee3e;
  --gold:#f2c81e;
  --orange:#faa54b;
  --ink:#1d1d1d;
  --text:#3a3a3a;
  --grey-panel:#efefef;
  --footer-top:#1e1e1e;
  --footer-bottom:#3a3a3a;
}
*{box-sizing:border-box;margin:0;padding:0}
html,body{width:1200px;height:3186px;overflow:hidden}
body{position:relative;background:#fff;font-family:"Open Sans",Arial,sans-serif;color:var(--text)}
.abs{position:absolute}
h1,h2,h3,.poppins{font-family:"Poppins",Arial,sans-serif}

/* hero */
.hero{left:0;top:0;width:1200px;height:690px;
  background:linear-gradient(180deg,#6b7a5a 0%,#8e9478 30%,#7c8a5c 55%,#a8725a 78%,#5d6a3c 100%)}
.hero-logo{left:80px;top:0;width:300px;height:85px;background:#fff;
  clip-path:polygon(0 0,100% 0,88% 100%,10% 100%)}
.brand{font-family:"Poppins",Arial,sans-serif;font-weight:700;letter-spacing:1px;color:#1e3563}
.hero-logo .brand{position:absolute;left:0;right:30px;top:22px;text-align:center;font-size:23px}
.nav{left:330px;top:0;width:782px;height:85px;
  background:linear-gradient(90deg,var(--blue),var(--deep-blue));
  clip-path:polygon(0 0,100% 0,93% 100%,5% 100%)}
.nav a{position:absolute;top:31px;color:#fff;font-family:"Poppins",Arial,sans-serif;font-size:16px;text-decoration:none;font-weight:500}
.hero-title{left:0;top:300px;width:1200px;text-align:center;color:#fff;font-size:48px;font-weight:600;line-height:56px;text-shadow:0 2px 6px rgba(0,0,0,.35)}
.hero-arrow{top:325px}

/* about */
.about-photo{left:98px;top:784px;width:395px;height:397px;background:linear-gradient(135deg,#c9a77c,#8c6a45 60%,#3e3a36)}
.about-box{left:404px;top:881px;width:696px;height:384px;background:var(--grey-panel);border:1px solid #d8d8d8;padding:38px 60px}
.about-box h2{font-size:34px;font-weight:500;color:var(--ink);margin-bottom:16px}
.about-box p{font-size:14.5px;line-height:24px;margin-bottom:20px;color:#444}
.btn{display:inline-block;background:linear-gradient(180deg,var(--yellow),var(--gold));color:var(--ink);font-family:"Poppins",Arial,sans-serif;font-weight:500}
.about-box .btn{width:143px;height:42px;line-height:42px;text-align:center;font-size:15px}

/* features */
.features{left:0;top:1370px;width:1200px;height:287px;background:linear-gradient(180deg,#2f6f7c,#3f8a8f 55%,#2c6a74)}
.feature{top:70px;width:250px;text-align:center;color:#fff}
.feature h3{font-size:21px;font-weight:500;margin-top:12px}
.feature p{font-size:12.5px;line-height:22px;margin-top:8px}
.divider{top:55px;width:1px;height:175px;background:rgba(255,255,255,.55)}

/* products */
.section-title{font-size:34px;font-weight:500;color:var(--ink);text-align:center;width:1200px;left:0}
.products-intro{left:0;top:1786px;width:1200px;text-align:center;font-size:17.5px;line-height:27px;color:#333}
.card{top:1882px;width:300px;height:195px}
.card .photo{height:136px}
.card .label{height:59px;line-height:59px;text-align:center;font-family:"Poppins",Arial,sans-serif;font-size:22px;color:var(--ink)}

/* catalogue */
.catalogue{left:0;top:2162px;width:1200px;height:155px;background:linear-gradient(90deg,var(--teal),var(--blue) 60%,var(--deep-blue))}
.catalogue h2{position:absolute;left:106px;top:54px;color:#fff;font-size:34px;font-weight:400;letter-spacing:.5px}
.catalogue .btn{position:absolute;left:928px;top:53px;width:171px;height:51px;line-height:51px;text-align:center;font-size:16px;border:1px solid #d7ae10}

/* find & contact */
.find h2,.contact h2{font-size:34px;font-weight:500;color:var(--ink)}
.find p.lead{font-size:13.5px;line-height:27px;color:#333;margin-top:16px;width:480px}
.info{left:100px;width:520px;height:56px}
.info .dot{position:absolute;left:0;top:0;width:56px;height:56px;border-radius:50%;background:var(--teal)}
.info span{position:absolute;left:74px;font-size:18px;line-height:26px;color:#222}
.field{left:660px;width:437px;border:1.5px solid #7b7b7b;background:#fff;font-size:12px;color:#555;padding:10px 22px}
.submit{left:973px;top:2683px;width:124px;height:41px;line-height:41px;text-align:center;font-size:15px;font-weight:600}

/* footer */
.footer{left:0;top:2810px;width:1200px;height:376px;background:linear-gradient(180deg,var(--footer-top),var(--footer-bottom))}
.footer .brand{position:absolute;left:153px;top:122px;color:#fff;font-size:22px}
.footer h4{position:absolute;top:70px;font-family:"Poppins",Arial,sans-serif;font-weight:500;font-size:20px;color:#fff}
.footer ul{position:absolute;top:124px;list-style:none;color:#fff;font-size:13.5px;line-height:28px}
.hours{position:absolute;left:605px;top:124px;color:#fff;font-size:13.5px;line-height:28px}
.hours b{font-weight:400;display:inline-block;width:75px}
.footer .rule{position:absolute;left:100px;top:297px;width:998px;height:1px;background:#888}
.copyright{position:absolute;left:100px;top:323px;color:#fff;font-size:13px}
.social{position:absolute;left:1069px;top:321px;width:28px;height:28px;border-radius:50%;background:var(--teal)}
</style>
</head>
<body>

<!-- hero slider -->
<div class="abs hero" role="img" aria-label="Hero slide: garden courtyard with timber fence, plants and a paved path"></div>
<div class="abs hero-logo"><span class="brand">BRELVOX LUMBER</span></div>
<nav class="abs nav">
  <a style="left:116px">HOME</a>
  <a style="left:239px">PRODUCTS</a>
  <a style="left:371px">QUOTES</a>
  <a style="left:496px">SPECIALS</a>
  <a style="left:641px">CONTACT US</a>
</nav>
<h1 class="abs hero-title">Melbourne’s Premier Timber<br>Decking Supplier</h1>
<svg class="abs hero-arrow" style="left:62px" width="40" height="74" viewBox="0 0 40 74"><polyline points="36,2 4,37 36,72" fill="none" stroke="#fff" stroke-width="3"/></svg>
<svg class="abs hero-arrow" style="left:1098px" width="40" height="74" viewBox="0 0 40 74"><polyline points="4,2 36,37 4,72" fill="none" stroke="#fff" stroke-width="3"/></svg>

<!-- about -->
<div class="abs about-photo" role="img" aria-label="Close-up of a claw hammer resting on timber planks"></div>
<section class="abs about-box">
  <h2>ABOUT US</h2>
  <p>We are a Melbourne timber fencing, decking and flooring supplier located in Kelmore Park (Ashvale), supplying quality materials such as timber fencing materials, steelform fencing, decking, Redgum Sleepers, Cypress Pickets and much more to most of Melbourne and surrounding suburbs.</p>
  <p>Our timber yard is open to both the trade and do-it-yourself market. If you are looking for quality timber fencing and decking products, look no further than Brelvox.</p>
  <a class="btn">Learn More</a>
</section>

<!-- feature links -->
<section class="abs features" role="group" aria-label="Quick sections">
  <div class="abs feature" style="left:75px">
    <svg width="58" height="58" viewBox="0 0 58 58"><path d="M29 4 52 15 29 26 6 15Z M6 19 27 29 27 54 6 43Z M52 19 31 29 31 54 52 43Z" fill="#fff"/></svg>
    <h3>PRODUCTS</h3><p>Browse through our wide<br>range of products</p>
  </div>
  <div class="abs divider" style="left:329px"></div>
  <div class="abs feature" style="left:338px">
    <svg width="70" height="58" viewBox="0 0 70 58"><rect x="8" y="10" width="56" height="40" rx="3" fill="#fff"/><rect x="2" y="16" width="10" height="28" fill="#fff"/><g fill="#3f8a8f"><rect x="22" y="18" width="34" height="4"/><rect x="22" y="27" width="34" height="4"/><rect x="22" y="36" width="34" height="4"/><rect x="14" y="18" width="4" height="4"/><rect x="14" y="27" width="4" height="4"/><rect x="14" y="36" width="4" height="4"/></g></svg>
    <h3>QUOTES</h3><p>After a Quote? Fill out our<br>online Quote form</p>
  </div>
  <div class="abs divider" style="left:599px"></div>
  <div class="abs feature" style="left:601px">
    <svg width="58" height="58" viewBox="0 0 58 58"><path d="M30 6 52 6 52 28 26 54 4 32Z" fill="#fff"/><circle cx="43" cy="15" r="4" fill="#3f8a8f"/></svg>
    <h3>SPECIALS</h3><p>Looking for a Deal<br>checkout our Specials</p>
  </div>
  <div class="abs divider" style="left:869px"></div>
  <div class="abs feature" style="left:865px">
    <svg width="58" height="58" viewBox="0 0 58 58"><path d="M14 6c3 0 7 9 7 11s-4 4-4 6c0 4 10 16 16 17 2 0 4-4 6-4s11 4 11 7c0 4-6 9-10 9C25 52 6 33 6 18c0-5 5-12 8-12Z" fill="#fff"/><path d="M34 8a16 16 0 0 1 16 16M34 16a8 8 0 0 1 8 8" fill="none" stroke="#fff" stroke-width="3"/></svg>
    <h3>CONTACT</h3><p>Got a Question ?<br>No Problem</p>
  </div>
</section>

<!-- products -->
<h2 class="abs section-title" style="top:1730px">OUR PRODUCTS</h2>
<p class="abs products-intro">We have an extensive range of quality timber fencing and decking products available at our<br>Kelmore Park timber yard. Products include:</p>
<svg class="abs" style="left:22px;top:1960px" width="24" height="42" viewBox="0 0 24 42"><polyline points="21,2 3,21 21,40" fill="none" stroke="#333" stroke-width="2.5"/></svg>
<svg class="abs" style="left:1154px;top:1960px" width="24" height="42" viewBox="0 0 24 42"><polyline points="3,2 21,21 3,40" fill="none" stroke="#333" stroke-width="2.5"/></svg>
<div class="abs card" style="left:98px">
  <div class="photo" role="img" aria-label="Stacked timber fencing boards" style="background:linear-gradient(180deg,#5a4636,#b98b60 55%,#d8b080)"></div>
  <div class="label" style="background:var(--lime)">Timber Fencing</div>
</div>
<div class="abs card" style="left:450px">
  <div class="photo" role="img" aria-label="Bundles of treated pine in a timber yard" style="background:linear-gradient(180deg,#4a4842,#8c8270 50%,#b0a48c)"></div>
  <div class="label" style="background:var(--sky)">Treated Pine</div>
</div>
<div class="abs card" style="left:801px">
  <div class="photo" role="img" aria-label="Stack of steel retaining wall posts" style="background:linear-gradient(180deg,#6e7272,#a5a9a8 50%,#80807a)"></div>
  <div class="label" style="background:var(--orange)">Retaining Wall Posts</div>
</div>

<!-- catalogue -->
<section class="abs catalogue">
  <h2>VISIT OUR ONLINE CATALOGUE</h2>
  <a class="btn">CLICK HERE</a>
</section>

<!-- find us -->
<section class="abs find" style="left:100px;top:2396px">
  <h2>IT'S EASY TO FIND US</h2>
  <p class="lead">Sed ut perspiciatis unde omnis iste natus error sit voluptatem accusantium do-loremque laudantium, totam rem aperiam</p>
</section>
<div class="abs info" style="top:2531px">
  <div class="dot"></div>
  <svg class="abs" style="left:18px;top:14px" width="20" height="28" viewBox="0 0 20 28"><path d="M10 0a10 10 0 0 1 10 10c0 7-10 18-10 18S0 17 0 10A10 10 0 0 1 10 0Z" fill="#fff"/><circle cx="10" cy="10" r="3.5" fill="#33b8a4"/></svg>
  <span style="top:2px">14 Harlow Court,<br>Kelmore Park (Ashvale) VIC 3091</span>
</div>
<div class="abs info" style="top:2601px">
  <div class="dot"></div>
  <svg class="abs" style="left:17px;top:17px" width="22" height="22" viewBox="0 0 58 58"><path d="M14 6c3 0 7 9 7 11s-4 4-4 6c0 4 10 16 16 17 2 0 4-4 6-4s11 4 11 7c0 4-6 9-10 9C25 52 6 33 6 18c0-5 5-12 8-12Z" fill="#fff"/></svg>
  <span style="top:15px">(03) 9000-4821</span>
</div>
<div class="abs info" style="top:2669px">
  <div class="dot"></div>
  <svg class="abs" style="left:16px;top:19px" width="24" height="18" viewBox="0 0 24 18"><rect width="24" height="18" rx="2" fill="#fff"/><polyline points="1,2 12,10 23,2" fill="none" stroke="#33b8a4" stroke-width="2"/></svg>
  <span style="top:15px">info@brelvoxlumber.com</span>
</div>

<!-- contact form -->
<section class="abs contact" style="left:658px;top:2392px"><h2>CONTACT US</h2></section>
<div class="abs field" style="top:2464px;height:44px">Name</div>
<div class="abs field" style="top:2523px;height:45px">Email</div>
<div class="abs field" style="top:2585px;height:83px">Message</div>
<a class="abs btn submit">SUBMIT</a>

<!-- footer -->
<footer class="abs footer">
  <span class="brand">BRELVOX LUMBER</span>
  <h4 style="left:399px">Quick Links</h4>
  <ul style="left:400px"><li>Home</li><li>Products</li><li>Quotes</li><li>Specials</li><li>Contact Us</li></ul>
  <h4 style="left:605px">Trading Hours</h4>
  <div class="hours">
    <div><b>Mon - Thur</b>: 7:00am to 4.30pm</div>
    <div><b>Friday</b>: 7:00am to 4.00pm</div>
    <div><b>Saturday</b>: 8am to 11am</div>
  </div>
  <h4 style="left:881px">Resources</h4>
  <ul style="left:883px;line-height:32px"><li>Terms and Conditions</li><li>Privacy Policy</li><li>Disclaimer</li></ul>
  <div class="rule"></div>
  <p class="copyright">Copyright © 2018. All Rights Reserved.</p>
  <div class="social"></div>
</footer>

</body>
</html>
```